CD-/Plattencover für Band
Zielgruppe
Bandname:
Glutwerk
Album Titel:
Nebelgrauer Pfad
Musikvideo:
https://www.clipwelle.example/watch?v=Q7T3kaPmXRe
Unsere Musik ist im wahrsten Sinn des Wortes Glutiger Pfad. Schwere Texte die nicht immer gut schmecken aber immer mit Lösungsansatz die in vielen Lebenslagen helfen und unterstützen sollen.
Nebelgraue Erzählungen“ wie man sie aus dem herausfordernden Leben kennt, verpackt in Stoffig Rockigen Sound.
Zielgruppe:
Musikinteressiert ab 25 Jahren / alleinstehende Mütter / Personen in Sinnkrisen / Personen die jemanden verloren haben / Personen mit psychischen Problemen / Personen die an einem Wendepunkt kommen / Personen die sich privat oder Beruflich verändern möchten
Positionierung:
Zusammenführung von modernem Heavy Rock und Mundart Texten, irgendwo zwischen Konrad von Wettlach und Zwirnbögl
Songinhalte:
Mobbing / Nostalgie / Beziehungen / Veränderungen / Trauer / Depression / Angststörung / Mut / Zusammenhalt / Liebe / Enttäuschungen / Selbstfindung / Musikindustrie
Aufgabenstellung
Das Bandfoto dient nur zur Info. Das Logo soll aufs Cover.
Design: Cool, Modern, Rockig, Bodenständig angelehnt und passend zum Logo.
Im Mittelpunkt soll ein Lollipop stehen der dann auch als Markenzeichen dienen soll. Mit dem Lollipop soll der Albumtitel(Nebelgrauer Pfad) dargestellt werden. Der Lolli steht für Süß. Für Bitter könnte der Lolli die Form eines Blattes haben oder er könnte eine außergewöhnliche Farbe haben oder es könnten sich Dornen und Blätter am Lollpop Stiel entlag schlingen. Die zentrale Farbe/Hintergrund soll Magenta sein.

```html
<!DOCTYPE html>
<html lang="de">
<head>
<meta charset="utf-8">
<title>Glutwerk – Albumcover</title>
<link rel="stylesheet" href="https://fonts.googleapis.com/css2?family=Kaushan+Script&display=swap">
<style>
  :root {
    --magenta: #cc64a0;
    --magenta-light: rgba(196, 160, 190, 0.6);
    --magenta-soft: rgba(190, 140, 180, 0.45);
    --navy: #27308a;
    --candy-red: #dd0c3f;
    --candy-deep: #c70f3a;
    --shadow-violet: #9c4f94;
    --title-white: #ffffff;
    --page: #ffffff;
  }
  html, body {
    margin: 0;
    padding: 0;
    width: 1200px;
    height: 1200px;
    overflow: hidden;
    background: var(--page);
  }
  .album-cover {
    position: relative;
    width: 1200px;
    height: 1200px;
    background: var(--magenta);
    overflow: hidden;
  }
  .cover-backdrop {
    position: absolute;
    inset: 0;
    width: 1200px;
    height: 1200px;
  }
  .backdrop-circle--upper { fill: var(--magenta-soft); }
  .backdrop-circle--centre { fill: var(--magenta-light); }
  .backdrop-line {
    fill: none;
    stroke: var(--navy);
    stroke-width: 2.5;
  }
  .band-name {
    position: absolute;
    left: 110px;
    top: 330px;
    margin: 0;
    font-family: "Kaushan Script", "Brush Script MT", cursive;
    font-weight: 400;
    font-size: 210px;
    line-height: 1;
    color: var(--title-white);
    transform: rotate(-24deg);
    transform-origin: left center;
    white-space: nowrap;
    z-index: 2;
  }
  .lollipop-artwork {
    position: absolute;
    left: 470px;
    top: 470px;
    width: 320px;
    height: 600px;
    border-radius: 160px;
    background: radial-gradient(ellipse 60% 40% at 50% 30%,
      var(--candy-red) 0%,
      var(--candy-deep) 55%,
      rgba(156, 79, 148, 0.55) 100%);
    z-index: 1;
  }
</style>
</head>
<body>
  <main class="album-cover">
    <svg class="cover-backdrop" viewBox="0 0 1200 1200" aria-hidden="true">
      <circle class="backdrop-circle--upper" cx="330" cy="-60" r="420"/>
      <circle class="backdrop-circle--centre" cx="720" cy="640" r="500"/>
      <circle class="backdrop-circle--upper" cx="1000" cy="300" r="320"/>
      <path class="backdrop-line" d="M0 330 C 90 330, 170 240, 200 130"/>
      <path class="backdrop-line" d="M1200 720 C 1110 760, 1040 900, 1060 1080"/>
    </svg>

    <h1 class="band-name">Glutwerk</h1>

    <div class="lollipop-artwork" role="img"
         aria-label="Illustration: roter Lollipop mit blauer Kappe auf weißem Stiel, um den sich eine dunkelblaue Dornenranke windet, darunter ein violetter Schatten"></div>
  </main>
</body>
</html>
```